Cosmetic Clinic Looking For Sign Designs

We are looking for sign design ideas for the front of our building and a lawn sign for our cosmetic injection salon.
I have uploaded the front of our building for a mock up and size, lawn posts with size and a sign that uses the same dimensions.
We would like both signs to be black for the background.

Target Market(s)

Ages 18-75

Industry/Entity Type

Beauty

Requirements
Must have
• Services we offer:
• Cosmetic Injections
• Airbrush Spray Tanning
• Eyelash Growth Serum
• Skin Care Products & More
• Everything must be on a black background
• The lawn sign must have the address: 483 Fenwick and the building sign should have the phone number.
Should not have
• Nothing can light up (no LED)
• Both signs do not need the full address. Just 483 Fenwick and the phone number

```html
<!DOCTYPE html>
<html lang="en">
<head>
<meta charset="utf-8">
<title>Bright Bloom Salon – Sign</title>
<link rel="stylesheet" href="https://fonts.googleapis.com/css2?family=Roboto+Condensed:wght@700&family=Open+Sans:wght@400&family=Arimo:wght@700&display=swap">
<style>
  :root {
    --page: #ffffff;
    --sign-black: #000000;
    --frame-navy: #1a2250;
    --accent-pink: #e8196f;
    --brand-teal: #2499b8;
    --mark-lavender: #7a80bf;
    --text-white: #ffffff;
  }
  * { box-sizing: border-box; }
  html, body {
    margin: 0;
    padding: 0;
    width: 1200px;
    height: 1200px;
    overflow: hidden;
    background: var(--page);
  }
  .artboard {
    position: relative;
    width: 1200px;
    height: 1200px;
    overflow: hidden;
  }
  .sign-shape {
    position: absolute;
    left: 0;
    top: 0;
    width: 1200px;
    height: 1200px;
  }
  .line {
    position: absolute;
    left: 6px;
    width: 1194px;
    margin: 0;
    padding: 0;
    text-align: center;
    white-space: nowrap;
  }
  .brand-mark-name {
    position: absolute;
    left: 522px;
    top: 253px;
    width: 162px;
    margin: 0;
    text-align: center;
    font-family: "Roboto Condensed", sans-serif;
    font-weight: 700;
    font-size: 27px;
    line-height: 33px;
    color: var(--text-white);
  }
  .brand-name {
    top: 402px;
    font-family: "Roboto Condensed", sans-serif;
    font-weight: 700;
    font-size: 74px;
    line-height: 80px;
    color: var(--brand-teal);
    letter-spacing: 1px;
  }
  .brand-sub {
    top: 480px;
    font-family: "Open Sans", sans-serif;
    font-weight: 400;
    font-size: 47px;
    line-height: 50px;
    color: var(--accent-pink);
  }
  .services-title {
    top: 591px;
    font-family: "Arimo", sans-serif;
    font-weight: 700;
    font-size: 44px;
    line-height: 50px;
    color: var(--accent-pink);
  }
  .services-list {
    top: 655px;
    list-style: none;
    font-family: "Arimo", sans-serif;
    font-weight: 700;
    font-size: 27px;
    line-height: 35px;
    color: var(--brand-teal);
  }
  .address {
    top: 880px;
    font-family: "Arimo", sans-serif;
    font-weight: 700;
    font-size: 31px;
    line-height: 38px;
    color: var(--text-white);
  }
  .phone {
    top: 926px;
    font-family: "Arimo", sans-serif;
    font-weight: 700;
    font-size: 57px;
    line-height: 62px;
    color: var(--text-white);
  }
</style>
</head>
<body>
<div class="artboard">
  <svg class="sign-shape" width="1200" height="1200" viewBox="0 0 1920 1920" aria-hidden="true">
    <path d="M488 1605 L488 510 Q488 450 548 450 L595 450 L595 430 Q595 380 650 380 L765 380 Q830 268 965 267 Q1100 268 1168 380 L1283 380 Q1338 380 1338 430 L1338 450 L1385 450 Q1445 450 1445 510 L1445 1605 Q1445 1665 1385 1665 L548 1665 Q488 1665 488 1605 Z"
          fill="var(--sign-black)" stroke="var(--frame-navy)" stroke-width="22"/>
    <circle cx="965" cy="460" r="132" fill="var(--mark-lavender)" stroke="var(--accent-pink)" stroke-width="14"/>
    <polygon points="620,803 825,799 825,808" fill="var(--accent-pink)"/>
    <polygon points="1107,799 1312,803 1107,808" fill="var(--accent-pink)"/>
    <polygon points="560,1367 965,1363 1380,1367 965,1371" fill="var(--accent-pink)"/>
    <polygon points="560,1610 965,1606 1380,1610 965,1614" fill="var(--accent-pink)"/>
  </svg>

  <div class="brand-mark-name">Bright<br>Bloom</div>

  <h1 class="line brand-name">BRIGHT BLOOM</h1>
  <p class="line brand-sub">SALON</p>

  <h2 class="line services-title">Services we offer:</h2>
  <ul class="line services-list">
    <li>- Cosmetic Injections</li>
    <li>- Airbrush Spray Tanning</li>
    <li>- Eyelash Growth Serum</li>
    <li>- Skin Care Products &amp; More</li>
  </ul>

  <p class="line address">483 Fenwick and the building</p>
  <p class="line phone">000 0000 000</p>
</div>
</body>
</html>
```